Veldon Tracing, Inc. - Stationary Project
Business Cards and Stationary for Missing Person Consultants
Professional
Luke Hammond
Search Coordinator
718 West Marlow Avenue
Suite #263
Orlando, FL 32806
lhammond@veldontracing-demo.org
www.VeldonTracing-demo.org
Our organization is called upon
when someone disappears. We¹d like to have a professional business card that
is very eye-catching and people will notice. Please use the red, black and
gray colors in the logo to make a great looking business card, letterhead
and envelope. We look forward to seeing your designs.
We'd like to see a clever use of the logo on the back of the card in bigger format.
This is our logo in AI format.

```html
<!DOCTYPE html>
<html lang="en">
<head>
<meta charset="utf-8">
<title>Veldon Tracing – Stationary Concepts</title>
<link rel="stylesheet" href="https://fonts.googleapis.com/css2?family=Roboto:wght@400;700;900&family=Cormorant+Garamond:wght@500&display=swap">
<style>
  :root {
    --bg-top: #17345c;
    --bg-mid: #0a1a33;
    --bg-bottom: #02070f;
    --paper: #ffffff;
    --red: #c4202b;
    --ink: #1c1c1e;
    --grey: #6d7076;
    --faint: #eceef1;
    --caption: #7b8ba3;
    --title-grey: #9aa3b0;
  }
  * { margin: 0; padding: 0; box-sizing: border-box; }
  html, body { width: 1200px; height: 614px; overflow: hidden; }
  body {
    font-family: "Roboto", Arial, sans-serif;
    background: radial-gradient(ellipse 70% 55% at 60% 8%, var(--bg-top), var(--bg-mid) 60%, var(--bg-bottom));
    position: relative;
  }
  .sheet { position: absolute; background: var(--paper); box-shadow: 0 3px 10px rgba(0,0,0,.45); overflow: hidden; }
  .caption { position: absolute; font-size: 6px; color: var(--caption); text-align: center; }

  .brand { display: flex; align-items: center; gap: 5px; }
  .brand-dot { border-radius: 50%; background: var(--red); flex: none; }
  .brand-name { font-weight: 900; color: var(--ink); letter-spacing: .03em; line-height: 1; }

  .watermark { position: absolute; border-radius: 50%; background: var(--faint); }

  .contact { font-size: 5px; color: var(--grey); line-height: 1.75; }
  .contact li { list-style: none; display: flex; align-items: center; gap: 3px; }
  .contact svg { width: 5px; height: 5px; fill: var(--red); flex: none; }

  /* business card front */
  .card-front { left: 36px; top: 138px; width: 235px; height: 134px; border-radius: 5px; }
  .card-front .brand { position: absolute; left: 14px; top: 14px; }
  .card-front .brand-dot { width: 24px; height: 24px; }
  .card-front .brand-name { font-size: 11px; }
  .card-front .watermark { width: 120px; height: 120px; right: -20px; top: 8px; }
  .card-front .person { position: absolute; right: 16px; top: 62px; text-align: right; }
  .person-name { font-size: 10px; font-weight: 700; color: var(--red); }
  .person-title { font-size: 5.5px; color: var(--grey); margin-top: 1px; }
  .card-front .address { position: absolute; left: 14px; top: 54px; font-size: 5px; color: var(--grey); line-height: 1.5; }
  .card-front .contact { position: absolute; left: 14px; top: 76px; }

  /* business card back */
  .card-back { left: 36px; top: 366px; width: 235px; height: 134px; border-radius: 5px; }
  .card-back .brand-dot { position: absolute; left: 99px; top: 26px; width: 38px; height: 38px; }
  .card-back .web { position: absolute; left: 0; right: 0; top: 96px; text-align: center; font-size: 5.5px; color: var(--ink); }

  /* letterhead */
  .letterhead { left: 295px; top: 36px; width: 401px; height: 511px; }
  .letterhead .brand { position: absolute; left: 14px; top: 30px; }
  .letterhead .brand-dot { width: 22px; height: 22px; }
  .letterhead .brand-name { font-size: 10px; }
  .letterhead .address { position: absolute; left: 254px; top: 24px; font-size: 5px; color: var(--grey); line-height: 1.5; }
  .letterhead .contact { position: absolute; left: 254px; top: 40px; }
  .letterhead .watermark { width: 140px; height: 140px; left: 130px; top: 300px; }

  /* presentation title */
  .title { position: absolute; left: 776px; top: 98px; width: 320px; }
  .title .brand { justify-content: center; gap: 10px; }
  .title .brand-dot { width: 58px; height: 58px; }
  .title .brand-name { font-size: 30px; color: #ffffff; }
  .title-sub { font-family: "Cormorant Garamond", Georgia, serif; font-size: 22px; color: var(--title-grey); text-align: center; margin-top: 8px; padding-left: 60px; }

  /* envelope */
  .envelope { left: 727px; top: 288px; width: 444px; height: 259px; }
  .envelope .flap { position: absolute; left: 0; top: 0; width: 444px; height: 70px; }
  .envelope .seal { position: absolute; left: 209px; top: 20px; width: 26px; height: 26px; border-radius: 50%; background: var(--red); }
  .envelope .brand { position: absolute; left: 14px; top: 80px; }
  .envelope .brand-dot { width: 22px; height: 22px; }
  .envelope .brand-name { font-size: 10px; }
  .envelope .address { position: absolute; left: 14px; top: 110px; font-size: 5px; color: var(--grey); line-height: 1.5; }
  .envelope .watermark { width: 150px; height: 150px; left: 300px; top: 96px; }
</style>
</head>
<body>

  <section class="sheet card-front" aria-label="Business card front">
    <div class="watermark"></div>
    <div class="brand"><span class="brand-dot"></span><span class="brand-name">VELDON TRACING</span></div>
    <div class="address">718 West Marlow Avenue<br>Suite #263 Orlando, FL 32806</div>
    <ul class="contact">
      <li><svg viewBox="0 0 10 10"><path d="M2 0h2l1 3-1.5 1a6 6 0 0 0 2.5 2.5L7 5l3 1v2a2 2 0 0 1-2 2A8 8 0 0 1 0 2a2 2 0 0 1 2-2z"/></svg>(407) 555-0148</li>
      <li><svg viewBox="0 0 10 10"><rect x="1" y="2" width="8" height="6"/></svg>(407) 555-0193</li>
      <li><svg viewBox="0 0 10 10"><path d="M0 2h10v6H0zM0 2l5 3 5-3"/></svg>lhammond@veldontracing-demo.org</li>
      <li><svg viewBox="0 0 10 10"><circle cx="5" cy="5" r="4.5"/></svg>www.VeldonTracing-demo.org</li>
    </ul>
    <div class="person">
      <div class="person-name">Luke Hammond</div>
      <div class="person-title">Search Coordinator</div>
    </div>
  </section>
  <p class="caption" style="left:36px;top:282px;width:235px;">Front card</p>

  <section class="sheet card-back" aria-label="Business card back">
    <span class="brand-dot"></span>
    <p class="web">www.VeldonTracing-demo.org</p>
  </section>
  <p class="caption" style="left:36px;top:508px;width:235px;">Back card</p>

  <section class="sheet letterhead" aria-label="Letterhead">
    <div class="brand"><span class="brand-dot"></span><span class="brand-name">VELDON TRACING</span></div>
    <div class="address">718 West Marlow Avenue<br>Suite #263 Orlando, FL 32806</div>
    <ul class="contact">
      <li><svg viewBox="0 0 10 10"><path d="M2 0h2l1 3-1.5 1a6 6 0 0 0 2.5 2.5L7 5l3 1v2a2 2 0 0 1-2 2A8 8 0 0 1 0 2a2 2 0 0 1 2-2z"/></svg>(407) 555-0148</li>
      <li><svg viewBox="0 0 10 10"><rect x="1" y="2" width="8" height="6"/></svg>(407) 555-0193</li>
      <li><svg viewBox="0 0 10 10"><path d="M0 2h10v6H0zM0 2l5 3 5-3"/></svg>lhammond@veldontracing-demo.org</li>
      <li><svg viewBox="0 0 10 10"><circle cx="5" cy="5" r="4.5"/></svg>www.VeldonTracing-demo.org</li>
    </ul>
    <div class="watermark"></div>
  </section>
  <p class="caption" style="left:295px;top:556px;width:401px;">Letterhead</p>

  <header class="title">
    <div class="brand"><span class="brand-dot"></span><span class="brand-name">VELDON TRACING</span></div>
    <p class="title-sub">Stationary Concepts</p>
  </header>

  <section class="sheet envelope" aria-label="Envelope">
    <svg class="flap" viewBox="0 0 444 70" preserveAspectRatio="none">
      <path d="M0 0L222 68L444 0" fill="none" stroke="#d9dce0" stroke-width="1"/>
    </svg>
    <span class="seal"></span>
    <div class="brand"><span class="brand-dot"></span><span class="brand-name">VELDON TRACING</span></div>
    <div class="address">718 West Marlow Avenue, Suite #263<br>Orlando, FL 32806</div>
    <div class="watermark"></div>
  </section>
  <p class="caption" style="left:727px;top:556px;width:444px;">Envelope</p>

</body>
</html>
```